Electronic Time-sheet & Training Tracker for Mobile phone

App should have two functions:Access by Quillon and Vextora:Employee Tracker: I need to be able to add/edit employees and personal information (example: address, DL number, SS number, DOB, employee number), drug screen information (type DCCHA and expiration date, DCCFO and expiration date, DCCHT and expiration date, PRAV Background and expiration date) and enter multiple training records (KEMB8 and expiration date). It would be great to receive an expiration alert.The employee would only have visibility to his own. Supervisors would have overall visibility.Time-Sheet:I need a time-sheet that can be accessed on the phone, be completed, then have the ability to electronically sign and submitted. The timesheet needs to be used two-fold for supervision to verify hours and edit (if need be), he would approve and forward to payroll. The time-sheet should be daily or weekly if we can get the data to fit. We are trying to streamline field supervisors having to log on to a computer to access a server just to do time-sheets. We need it to be user-friendly. We need to have two places to have electronic signatures (employee and supervisor).
A couple of designers have asked for an additional day. Others are making changes based on feedback.
Industrial (Oil ad Gas)
- Timesheet portion may require multiple entries with billable, non-billable, shop drop-down and job number and category code (LRS, HTS, FMS, ITP, OBS, HTT, NDE)
- Tracker - Training expiration alert or notifications by email to employee and supervisors.

```html
<!DOCTYPE html>
<html lang="en">
<head>
<meta charset="utf-8">
<title>Profile – Role Access Screens</title>
<link href="https://fonts.googleapis.com/css2?family=Open+Sans:wght@400;600;700&family=Oswald:wght@400;500&family=Source+Serif+4:wght@400;500&display=swap" rel="stylesheet">
<style>
:root{
  --board:#888888;
  --ink:#222222;
  --bar:#231f20;
  --orange:#d4601a;
  --line:#333333;
  --line-soft:#e3e3e3;
  --muted:#a8a8a8;
  --ok:#1f9a3e;
  --bad:#d8232a;
  --white:#ffffff;
}
*{box-sizing:border-box;margin:0;padding:0}
html,body{width:848px;height:1200px;overflow:hidden}
body{background:var(--board);font-family:"Open Sans",sans-serif;color:var(--ink);position:relative}
.caption{position:absolute;width:250px;text-align:center;color:var(--white);font-family:"Source Serif 4",serif;font-size:12px;line-height:16.6px}
.caption.top{top:59px}
.caption.bottom{top:1115px}
.screen{position:absolute;top:108px;width:239px;height:990px;background:var(--white);border-radius:22px;overflow:hidden}
.topbar{background:var(--bar);height:55px;color:var(--white)}
.status{height:28px;display:flex;align-items:center;justify-content:space-between;padding:0 22px 0 26px;font-size:6.5px}
.status svg{width:30px;height:6px;fill:var(--white)}
.appbar{height:27px;display:flex;align-items:center;justify-content:space-between;padding:0 14px 0 12px}
.appbar h1{font-family:"Oswald",sans-serif;font-weight:400;font-size:10px;letter-spacing:.2px}
.menu{width:11px;height:8px;stroke:var(--white);stroke-width:1.3}
.bell{position:relative;width:12px;height:12px}
.bell svg{width:10px;height:11px;fill:var(--white)}
.badge{position:absolute;top:-5px;right:-5px;width:8px;height:8px;border-radius:50%;background:var(--orange);font-size:5px;line-height:8px;text-align:center;color:var(--white);font-weight:700}
.content{padding:0 10px}
.profile{height:79px;display:flex;align-items:flex-start;padding-top:27px;gap:6px;position:relative}
.avatar{width:26px;height:26px;border-radius:50%;background:var(--bar);display:flex;align-items:center;justify-content:center}
.avatar svg{width:12px;height:12px;fill:var(--white)}
.who{padding-top:3px}
.role{font-size:6px;font-weight:600;color:var(--orange);letter-spacing:.3px;line-height:8px}
.name{font-size:10px;font-weight:700;line-height:12px}
.name small{font-size:6.5px;font-weight:400}
.picker{position:absolute;right:2px;top:41px;width:10px;height:6px;stroke:var(--orange);stroke-width:1.4;fill:none}
.field{margin-bottom:18.2px}
.label{display:block;font-size:6.8px;font-weight:700;text-transform:uppercase;line-height:9px;letter-spacing:.2px}
.label-row{display:grid;grid-template-columns:108px 1fr}
.label-row .sub{font-weight:400;text-transform:none}
.box{height:30px;border:1px solid var(--line);display:flex;align-items:center;padding:0 10px;font-size:9.5px;gap:5px;background:var(--white)}
.box.locked{border-color:var(--line-soft);color:var(--muted)}
.pair{display:grid;grid-template-columns:109px 1fr}
.pair .box+.box{margin-left:-1px}
.chev{width:9px;height:5px;margin-left:auto;stroke:currentColor;stroke-width:1.2;fill:none}
.cal{width:9px;height:9px;margin-left:auto;stroke:currentColor;stroke-width:.9;fill:none}
.box.locked .cal,.box.locked .chev{stroke:#c8c8c8}
.dot{width:9px;height:9px;border-radius:50%;display:inline-block;flex:none}
.dot.ok{background:var(--ok)}
.dot.bad{background:var(--bad)}
.section{display:flex;align-items:center;gap:6px;margin:-7px -10px 18px 0;height:12px}
.section h2{font-family:"Oswald",sans-serif;font-weight:400;font-size:10.5px;color:var(--orange);white-space:nowrap}
.section span{flex:1;height:1px;background:var(--orange)}
.actions{display:flex;gap:6px;padding-left:28px;margin-top:11px}
.btn{height:30px;border-radius:3px;font-family:"Oswald",sans-serif;font-size:11px;display:flex;align-items:center;justify-content:center;gap:4px}
.btn.cancel{width:61px;border:1px solid var(--orange);color:var(--orange)}
.btn.save{width:117px;background:var(--orange);color:var(--white);font-weight:500}
.btn.save svg{width:9px;height:9px;fill:var(--white)}
.home{position:absolute;bottom:6px;left:77px;width:85px;height:2px;background:#eeeeee;border-radius:2px}
</style>
</head>
<body>

<p class="caption top" style="left:32px">EMPLOYEE can access only his/her records and can modify limited info.</p>
<p class="caption top" style="left:299px">SUPERVISOR has overall visibility and can modify more info.</p>
<p class="caption top" style="left:567px;top:76px">People w/ ADMIN role can modify all info.</p>

<!-- Employee role -->
<section class="screen" style="left:37px">
  <header class="topbar">
    <div class="status"><span>5:30</span><svg viewBox="0 0 30 6"><rect x="0" y="4" width="1.5" height="2"/><rect x="2.5" y="3" width="1.5" height="3"/><rect x="5" y="1.5" width="1.5" height="4.5"/><rect x="7.5" y="0" width="1.5" height="6"/><path d="M12 2.5a6 6 0 0 1 8 0l-1 1a4.5 4.5 0 0 0-6 0zM14 4.5a3 3 0 0 1 4 0L16 6z"/><rect x="23" y="1.5" width="7" height="3" rx="1"/></svg></div>
    <div class="appbar">
      <svg class="menu" viewBox="0 0 11 8"><path d="M0 .7h11M0 4h11M0 7.3h11"/></svg>
      <h1>PROFILE</h1>
      <div class="bell"><svg viewBox="0 0 10 11"><path d="M5 0.5a1 1 0 0 1 1 1 3.5 3.5 0 0 1 2.5 3.4V8l1 1.2H.5L1.5 8V4.9A3.5 3.5 0 0 1 4 1.5a1 1 0 0 1 1-1zM3.8 9.8h2.4a1.2 1.2 0 0 1-2.4 0z"/></svg><span class="badge">2</span></div>
    </div>
  </header>
  <div class="content">
    <div class="profile">
      <div class="avatar"><svg viewBox="0 0 12 12"><circle cx="6" cy="3.5" r="2.6"/><path d="M1 12a5 5 0 0 1 10 0z"/></svg></div>
      <div class="who"><p class="role">EMPLOYEE</p><p class="name">John Doe <small>(Employee#)</small></p></div>
    </div>
    <div class="field"><span class="label">Email</span><div class="box">JohnDoe@mailbox.example</div></div>
    <div class="field"><span class="label">Phone#</span><div class="box">123.456.7890</div></div>
    <div class="field"><span class="label">Address</span><div class="box">123 Main Street</div></div>
    <div class="field"><span class="label">City</span><div class="box">Stonebrook</div></div>
    <div class="field"><div class="label label-row"><span>State</span><span>Zip</span></div><div class="pair"><div class="box">MT<svg class="chev" viewBox="0 0 9 5"><path d="M.5.5l4 4 4-4"/></svg></div><div class="box">59414</div></div></div>
    <div class="field"><span class="label">DOB</span><div class="box locked">January 1, 2000<svg class="cal" viewBox="0 0 9 9"><rect x=".5" y="1.5" width="8" height="7"/><path d="M.5 3.5h8M2.5 0v2M6.5 0v2"/></svg></div></div>
    <div class="field"><span class="label">SS Number</span><div class="box locked">000-00-0000</div></div>
    <div class="field"><div class="label label-row"><span>DL Number</span><span>State Issued</span></div><div class="pair"><div class="box locked">123456789000</div><div class="box locked">MT<svg class="chev" viewBox="0 0 9 5"><path d="M.5.5l4 4 4-4"/></svg></div></div></div>
    <div class="field"><span class="label">DL Expiration Date</span><div class="box locked"><i class="dot ok"></i>August 15, 2020<svg class="cal" viewBox="0 0 9 9"><rect x=".5" y="1.5" width="8" height="7"/><path d="M.5 3.5h8M2.5 0v2M6.5 0v2"/></svg></div></div>
    <div class="section"><h2>DRUG SCREEN</h2><span></span></div>
    <div class="field"><div class="label label-row"><span>DCCHA</span><span class="sub">EXP. date</span></div><div class="pair"><div class="box locked"><i class="dot ok"></i>OK<svg class="chev" viewBox="0 0 9 5"><path d="M.5.5l4 4 4-4"/></svg></div><div class="box locked">12/31/2020<svg class="cal" viewBox="0 0 9 9"><rect x=".5" y="1.5" width="8" height="7"/><path d="M.5 3.5h8M2.5 0v2M6.5 0v2"/></svg></div></div></div>
    <div class="field"><div class="label label-row"><span>DCCFO</span><span class="sub">EXP. date</span></div><div class="pair"><div class="box locked"><i class="dot ok"></i>OK<svg class="chev" viewBox="0 0 9 5"><path d="M.5.5l4 4 4-4"/></svg></div><div class="box locked">06/10/2020<svg class="cal" viewBox="0 0 9 9"><rect x=".5" y="1.5" width="8" height="7"/><path d="M.5 3.5h8M2.5 0v2M6.5 0v2"/></svg></div></div></div>
    <div class="field"><div class="label label-row"><span>DCCHT</span><span class="sub">EXP. date</span></div><div class="pair"><div class="box locked"><i class="dot bad"></i>EXPIRED<svg class="chev" viewBox="0 0 9 5"><path d="M.5.5l4 4 4-4"/></svg></div><div class="box locked">02/01/2019<svg class="cal" viewBox="0 0 9 9"><rect x=".5" y="1.5" width="8" height="7"/><path d="M.5 3.5h8M2.5 0v2M6.5 0v2"/></svg></div></div></div>
    <div class="field"><div class="label label-row"><span>PRAV Background</span><span class="sub">EXP. date</span></div><div class="pair"><div class="box locked"><i class="dot ok"></i>OK<svg class="chev" viewBox="0 0 9 5"><path d="M.5.5l4 4 4-4"/></svg></div><div class="box locked">10/25/2020<svg class="cal" viewBox="0 0 9 9"><rect x=".5" y="1.5" width="8" height="7"/><path d="M.5 3.5h8M2.5 0v2M6.5 0v2"/></svg></div></div></div>
    <div class="actions"><div class="btn cancel">Cancel</div><div class="btn save"><svg viewBox="0 0 9 9"><path d="M0 0l9 4.5L0 9l1.5-4.5z"/></svg>SAVE</div></div>
  </div>
  <span class="home"></span>
</section>

<!-- Supervisor role -->
<section class="screen" style="left:305px">
  <header class="topbar">
    <div class="status"><span>5:30</span><svg viewBox="0 0 30 6"><rect x="0" y="4" width="1.5" height="2"/><rect x="2.5" y="3" width="1.5" height="3"/><rect x="5" y="1.5" width="1.5" height="4.5"/><rect x="7.5" y="0" width="1.5" height="6"/><path d="M12 2.5a6 6 0 0 1 8 0l-1 1a4.5 4.5 0 0 0-6 0zM14 4.5a3 3 0 0 1 4 0L16 6z"/><rect x="23" y="1.5" width="7" height="3" rx="1"/></svg></div>
    <div class="appbar">
      <svg class="menu" viewBox="0 0 11 8"><path d="M0 .7h11M0 4h11M0 7.3h11"/></svg>
      <h1>PROFILE</h1>
      <div class="bell"><svg viewBox="0 0 10 11"><path d="M5 0.5a1 1 0 0 1 1 1 3.5 3.5 0 0 1 2.5 3.4V8l1 1.2H.5L1.5 8V4.9A3.5 3.5 0 0 1 4 1.5a1 1 0 0 1 1-1zM3.8 9.8h2.4a1.2 1.2 0 0 1-2.4 0z"/></svg><span class="badge">5</span></div>
    </div>
  </header>
  <div class="content">
    <div class="profile">
      <div class="avatar"><svg viewBox="0 0 12 12"><circle cx="6" cy="3.5" r="2.6"/><path d="M1 12a5 5 0 0 1 10 0z"/></svg></div>
      <div class="who"><p class="role">EMPLOYEE</p><p class="name">John Doe <small>(Employee#)</small></p></div>
      <svg class="picker" viewBox="0 0 10 6"><path d="M.7.7L5 5 9.3.7"/></svg>
    </div>
    <div class="field"><span class="label">Email</span><div class="box">JohnDoe@mailbox.example</div></div>
    <div class="field"><span class="label">Phone#</span><div class="box">123.456.7890</div></div>
    <div class="field"><span class="label">Address</span><div class="box">123 Main Street</div></div>
    <div class="field"><span class="label">City</span><div class="box">Stonebrook</div></div>
    <div class="field"><div class="label label-row"><span>State</span><span>Zip</span></div><div class="pair"><div class="box">MT<svg class="chev" viewBox="0 0 9 5"><path d="M.5.5l4 4 4-4"/></svg></div><div class="box">59414</div></div></div>
    <div class="field"><span class="label">DOB</span><div class="box locked">January 1, 2000<svg class="cal" viewBox="0 0 9 9"><rect x=".5" y="1.5" width="8" height="7"/><path d="M.5 3.5h8M2.5 0v2M6.5 0v2"/></svg></div></div>
    <div class="field"><span class="label">SS Number</span><div class="box locked">000-00-0000</div></div>
    <div class="field"><div class="label label-row"><span>DL Number</span><span>State Issued</span></div><div class="pair"><div class="box">123456789000</div><div class="box">MT<svg class="chev" viewBox="0 0 9 5"><path d="M.5.5l4 4 4-4"/></svg></div></div></div>
    <div class="field"><span class="label">DL Expiration Date</span><div class="box"><i class="dot ok"></i>August 15, 2020<svg class="cal" viewBox="0 0 9 9"><rect x=".5" y="1.5" width="8" height="7"/><path d="M.5 3.5h8M2.5 0v2M6.5 0v2"/></svg></div></div>
    <div class="section"><h2>DRUG SCREEN</h2><span></span></div>
    <div class="field"><div class="label label-row"><span>DCCHA</span><span class="sub">EXP. date</span></div><div class="pair"><div class="box"><i class="dot ok"></i>OK<svg class="chev" viewBox="0 0 9 5"><path d="M.5.5l4 4 4-4"/></svg></div><div class="box">12/31/2020<svg class="cal" viewBox="0 0 9 9"><rect x=".5" y="1.5" width="8" height="7"/><path d="M.5 3.5h8M2.5 0v2M6.5 0v2"/></svg></div></div></div>
    <div class="field"><div class="label label-row"><span>DCCFO</span><span class="sub">EXP. date</span></div><div class="pair"><div class="box"><i class="dot ok"></i>OK<svg class="chev" viewBox="0 0 9 5"><path d="M.5.5l4 4 4-4"/></svg></div><div class="box">06/10/2020<svg class="cal" viewBox="0 0 9 9"><rect x=".5" y="1.5" width="8" height="7"/><path d="M.5 3.5h8M2.5 0v2M6.5 0v2"/></svg></div></div></div>
    <div class="field"><div class="label label-row"><span>DCCHT</span><span class="sub">EXP. date</span></div><div class="pair"><div class="box"><i class="dot bad"></i>EXPIRED<svg class="chev" viewBox="0 0 9 5"><path d="M.5.5l4 4 4-4"/></svg></div><div class="box">02/01/2019<svg class="cal" viewBox="0 0 9 9"><rect x=".5" y="1.5" width="8" height="7"/><path d="M.5 3.5h8M2.5 0v2M6.5 0v2"/></svg></div></div></div>
    <div class="field"><div class="label label-row"><span>PRAV Background</span><span class="sub">EXP. date</span></div><div class="pair"><div class="box"><i class="dot ok"></i>OK<svg class="chev" viewBox="0 0 9 5"><path d="M.5.5l4 4 4-4"/></svg></div><div class="box">10/25/2020<svg class="cal" viewBox="0 0 9 9"><rect x=".5" y="1.5" width="8" height="7"/><path d="M.5 3.5h8M2.5 0v2M6.5 0v2"/></svg></div></div></div>
    <div class="actions"><div class="btn cancel">Cancel</div><div class="btn save"><svg viewBox="0 0 9 9"><path d="M0 0l9 4.5L0 9l1.5-4.5z"/></svg>SAVE</div></div>
  </div>
  <span class="home"></span>
</section>

<!-- Admin role -->
<section class="screen" style="left:573px">
  <header class="topbar">
    <div class="status"><span>5:30</span><svg viewBox="0 0 30 6"><rect x="0" y="4" width="1.5" height="2"/><rect x="2.5" y="3" width="1.5" height="3"/><rect x="5" y="1.5" width="1.5" height="4.5"/><rect x="7.5" y="0" width="1.5" height="6"/><path d="M12 2.5a6 6 0 0 1 8 0l-1 1a4.5 4.5 0 0 0-6 0zM14 4.5a3 3 0 0 1 4 0L16 6z"/><rect x="23" y="1.5" width="7" height="3" rx="1"/></svg></div>
    <div class="appbar">
      <svg class="menu" viewBox="0 0 11 8"><path d="M0 .7h11M0 4h11M0 7.3h11"/></svg>
      <h1>PROFILE</h1>
      <div class="bell"><svg viewBox="0 0 10 11"><path d="M5 0.5a1 1 0 0 1 1 1 3.5 3.5 0 0 1 2.5 3.4V8l1 1.2H.5L1.5 8V4.9A3.5 3.5 0 0 1 4 1.5a1 1 0 0 1 1-1zM3.8 9.8h2.4a1.2 1.2 0 0 1-2.4 0z"/></svg><span class="badge">10</span></div>
    </div>
  </header>
  <div class="content">
    <div class="profile">
      <div class="avatar"><svg viewBox="0 0 12 12"><circle cx="6" cy="3.5" r="2.6"/><path d="M1 12a5 5 0 0 1 10 0z"/></svg></div>
      <div class="who"><p class="role">EMPLOYEE</p><p class="name">John Doe <small>(Employee#)</small></p></div>
      <svg class="picker" viewBox="0 0 10 6"><path d="M.7.7L5 5 9.3.7"/></svg>
    </div>
    <div class="field"><span class="label">Email</span><div class="box">JohnDoe@mailbox.example</div></div>
    <div class="field"><span class="label">Phone#</span><div class="box">123.456.7890</div></div>
    <div class="field"><span class="label">Address</span><div class="box">123 Main Street</div></div>
    <div class="field"><span class="label">City</span><div class="box">Stonebrook</div></div>
    <div class="field"><div class="label label-row"><span>State</span><span>Zip</span></div><div class="pair"><div class="box">MT<svg class="chev" viewBox="0 0 9 5"><path d="M.5.5l4 4 4-4"/></svg></div><div class="box">59414</div></div></div>
    <div class="field"><span class="label">DOB</span><div class="box">January 1, 2000<svg class="cal" viewBox="0 0 9 9"><rect x=".5" y="1.5" width="8" height="7"/><path d="M.5 3.5h8M2.5 0v2M6.5 0v2"/></svg></div></div>
    <div class="field"><span class="label">SS Number</span><div class="box">000-00-0000</div></div>
    <div class="field"><div class="label label-row"><span>DL Number</span><span>State Issued</span></div><div class="pair"><div class="box">123456789000</div><div class="box">MT<svg class="chev" viewBox="0 0 9 5"><path d="M.5.5l4 4 4-4"/></svg></div></div></div>
    <div class="field"><span class="label">DL Expiration Date</span><div class="box"><i class="dot ok"></i>August 15, 2020<svg class="cal" viewBox="0 0 9 9"><rect x=".5" y="1.5" width="8" height="7"/><path d="M.5 3.5h8M2.5 0v2M6.5 0v2"/></svg></div></div>
    <div class="section"><h2>DRUG SCREEN</h2><span></span></div>
    <div class="field"><div class="label label-row"><span>DCCHA</span><span class="sub">EXP. date</span></div><div class="pair"><div class="box"><i class="dot ok"></i>OK<svg class="chev" viewBox="0 0 9 5"><path d="M.5.5l4 4 4-4"/></svg></div><div class="box">12/31/2020<svg class="cal" viewBox="0 0 9 9"><rect x=".5" y="1.5" width="8" height="7"/><path d="M.5 3.5h8M2.5 0v2M6.5 0v2"/></svg></div></div></div>
    <div class="field"><div class="label label-row"><span>DCCFO</span><span class="sub">EXP. date</span></div><div class="pair"><div class="box"><i class="dot ok"></i>OK<svg class="chev" viewBox="0 0 9 5"><path d="M.5.5l4 4 4-4"/></svg></div><div class="box">06/10/2020<svg class="cal" viewBox="0 0 9 9"><rect x=".5" y="1.5" width="8" height="7"/><path d="M.5 3.5h8M2.5 0v2M6.5 0v2"/></svg></div></div></div>
    <div class="field"><div class="label label-row"><span>DCCHT</span><span class="sub">EXP. date</span></div><div class="pair"><div class="box"><i class="dot bad"></i>EXPIRED<svg class="chev" viewBox="0 0 9 5"><path d="M.5.5l4 4 4-4"/></svg></div><div class="box">02/01/2019<svg class="cal" viewBox="0 0 9 9"><rect x=".5" y="1.5" width="8" height="7"/><path d="M.5 3.5h8M2.5 0v2M6.5 0v2"/></svg></div></div></div>
    <div class="field"><div class="label label-row"><span>PRAV Background</span><span class="sub">EXP. date</span></div><div class="pair"><div class="box"><i class="dot ok"></i>OK<svg class="chev" viewBox="0 0 9 5"><path d="M.5.5l4 4 4-4"/></svg></div><div class="box">10/25/2020<svg class="cal" viewBox="0 0 9 9"><rect x=".5" y="1.5" width="8" height="7"/><path d="M.5 3.5h8M2.5 0v2M6.5 0v2"/></svg></div></div></div>
    <div class="actions"><div class="btn cancel">Cancel</div><div class="btn save"><svg viewBox="0 0 9 9"><path d="M0 0l9 4.5L0 9l1.5-4.5z"/></svg>SAVE</div></div>
  </div>
  <span class="home"></span>
</section>

<p class="caption bottom" style="left:32px">Expiration alert/notifications will be sent to the employee and the supervisors. (That is more related to App development/coding)</p>
<p class="caption bottom" style="left:299px">SUPERVISOR can select the employee using the dropdown menu (or the pop-up window), which is accessed by clicking on the orange arrow, next to the employee name.</p>

</body>
</html>
```